Software Company Banner Ad

We need a banner ad in two sizes. 728x90 and 300x250.
They should have strong similarity to the following ads:
http://www.vexlo.net/search/results?brand[0]=quorp&ad=4821396
http://www.vexlo.net/search/results?brand[0]=dravensoft&ad=4830517
Idea will be very similar. We want the same grey color, white text, and a realistic owl that blinks. The owl should have dramatic, bright, yellow eyes. The text will animate "from the top" as in the example. Though the logo animation will be different, all text and non-logo animation should match the animation in the example advertisements. The text will rotate between the following four sentences and images.
Looking for a provider of procurement cloud apps?
[Images - attached below]
The experts really liked our KTV booth.
Get great results with every procurement. [Learn more]
There are three vector files attached below. Feel free to change the colors as necessary to match the color scheme of the ad. We need one 2013 and one 2014 award in the ad.
The awards could appear simultaneously, could swap with each other or could appear in succession. Animation is acceptable.
There is an additional vector file with the company logo. The company logo should go where the Quorp logo is in horizontal ad. The company logo should go where the Dravensoft logo is in the block ad. The example ad has two logos. We will only need one logo on our ads. The logo should be changed to the color of the text used for the ad (white).
The owls eyes should slowly blink two times (as in the example).
The owl eyes should immediately grab someone's attention and all colors should compliment these eyes.
The [Learn more] button should have animation. The button should match the color of the owl's eyes. There should be a line/gleam/glare of light that travels across the button. The button should be embossed with the subtle animation occurring each time it appears.
Ads should be done with flash. We will need the source files and the names of any fonts used at the end of the project.
Thank you and please do not hesitate to contact with any questions.
Reason: We have contacted several photographers to see if the alternative owl images are available on Pixvane, Framelodge or similar. The duration extension is to accommodate this.
Target Market(s)
Target customers are procurement department employees of large companies.
Industry/Entity Type
It Company

```html
<!DOCTYPE html>
<html lang="en">
<head>
<meta charset="utf-8">
<title>Procurement Cloud Apps Banner 300x250</title>
<link rel="stylesheet" href="https://fonts.googleapis.com/css2?family=Raleway:wght@400;700&display=swap">
<style>
  :root {
    --stage-light: #fbfbfb;
    --stage-dark: #d9d9d9;
    --ad-border: #1f1f1f;
    --band-grey: #58595b;
    --text-white: #ffffff;
    --feather-deep: #3b2413;
    --feather-brown: #7a4a22;
    --feather-orange: #c67a34;
    --feather-amber: #e0a455;
    --feather-pale: #cfc6bb;
    --feather-grey: #8d8883;
    --eye-yellow: #f2d21a;
  }
  * { margin: 0; padding: 0; box-sizing: border-box; }
  html, body {
    width: 1200px;
    height: 1169px;
    overflow: hidden;
  }
  body {
    position: relative;
    background: radial-gradient(ellipse at 50% 42%, var(--stage-light) 0%, #efefef 45%, var(--stage-dark) 100%);
    font-family: "Raleway", sans-serif;
  }
  .banner {
    position: absolute;
    left: 239px;
    top: 224px;
    width: 723px;
    height: 600px;
    border: 2px solid var(--ad-border);
    overflow: hidden;
    background: var(--band-grey);
  }
  .banner__photo {
    position: absolute;
    left: 0;
    top: 0;
    width: 100%;
    height: 373px;
    background:
      linear-gradient(180deg, rgba(59,36,19,0.85) 0%, rgba(59,36,19,0) 22%),
      radial-gradient(ellipse 30% 45% at 50% 100%, var(--feather-pale) 0%, var(--feather-grey) 45%, rgba(141,136,131,0) 100%),
      radial-gradient(ellipse 55% 50% at 50% 60%, rgba(242,210,26,0.35) 0%, rgba(242,210,26,0) 70%),
      linear-gradient(90deg, var(--feather-brown) 0%, var(--feather-orange) 18%, var(--feather-amber) 35%, var(--feather-orange) 50%, var(--feather-amber) 65%, var(--feather-orange) 82%, var(--feather-brown) 100%),
      var(--feather-deep);
  }
  .banner__band {
    position: absolute;
    left: 0;
    top: 373px;
    width: 100%;
    height: 227px;
    background: var(--band-grey);
  }
  .banner__headline {
    position: absolute;
    left: 26px;
    top: 24px;
    color: var(--text-white);
    font-weight: 400;
    font-size: 38px;
    line-height: 55px;
    letter-spacing: 0.2px;
  }
  .banner__logo {
    position: absolute;
    right: 8px;
    bottom: 10px;
    color: var(--text-white);
    font-weight: 700;
    font-size: 40px;
    line-height: 1;
    letter-spacing: 1px;
  }
</style>
</head>
<body>
  <div class="banner">
    <div class="banner__photo" role="img" aria-label="Close-up photograph of an owl staring forward with dramatic bright yellow eyes, orange-brown feathers and a pale grey beak area"></div>
    <div class="banner__band">
      <p class="banner__headline">Looking for a provider<br>of procurement cloud apps?</p>
      <div class="banner__logo">NOVRA</div>
    </div>
  </div>
</body>
</html>
```